Buchcover-Design für Liebesgedichte
Zielgruppe
Ich möchte meine Liebesgedichte veröffentlichen.
Zielgruppe sind Frauen, Verliebte, Unglücklich Verliebte, frisch Getrennte
Aufgabenstellung
Titel: Kein Morgen trägt so leise fort
Untertitel: Verse zum Atemholen für Suchende
Das von mir vorlegte Cover sollte die Liebe ausdrücken. Durch das liegende Herz und durch die schwarz-rote fliessende Farbgebung im Hintergrund wollte ich ausdrücken, dass die Liebe und der Tod nah verwandt sind. Die Gedichte tragen dazu bei, als Liebender zu überleben. Damit ist gemeint, dass Liebende sich auf den unvermeidbaren Schmerz und die Verletzbarkeit in der Liebe einlassen müssen, um nicht dem kitschigen Liebesbegriff der Medien zu verfallen. Deshalb ist mir auch der Untertitel so wichtig.
Es sind aber auch ganz andere Gestaltungen möglich. Ist nur ein laienhafter Versuch von mir gewesen, auszudrücken, was ich im Cover sagen möchte

```html
<!DOCTYPE html>
<html lang="de">
<head>
<meta charset="utf-8">
<title>Kein Morgen trägt so leise fort – Buchumschlag</title>
<link rel="stylesheet" href="https://fonts.googleapis.com/css2?family=Pathway+Gothic+One&family=Oswald:wght@600;700&family=Pinyon+Script&display=swap">
<style>
  :root {
    --page: #ffffff;
    --cover: #050404;
    --rose: #dcb4a8;
    --rust: #8c3b2d;
    --silver: #dcdcdc;
    --ember: #6b2612;
    --flame: #f0b04a;
  }
  * { margin: 0; padding: 0; box-sizing: border-box; }
  html, body {
    width: 862px; height: 1200px; overflow: hidden;
    background: var(--page);
  }
  .spread {
    position: absolute;
    left: 34px; top: 316px;
    width: 794px; height: 568px;
    background: var(--cover);
    overflow: hidden;
  }
  .thin {
    font-family: "Pathway Gothic One", "Oswald", sans-serif;
    color: var(--rose);
    text-transform: uppercase;
  }

  /* Rückseite */
  .back-smoke {
    position: absolute; left: 20px; top: 55px;
    width: 320px; height: 470px;
    background: radial-gradient(ellipse at 50% 42%, rgba(120,45,20,.55) 0%, rgba(80,28,12,.35) 40%, rgba(5,4,4,0) 70%);
  }
  .blurb {
    position: absolute; left: 30px; top: 111px; width: 300px;
    font-family: "Pathway Gothic One", sans-serif;
    color: var(--rose);
    font-size: 14.5px; line-height: 19px;
    letter-spacing: 2.2px; text-align: center;
  }

  /* Buchrücken */
  .spine-subtitle {
    position: absolute; left: 386px; top: 10px; height: 136px;
    writing-mode: vertical-rl; transform: rotate(180deg);
    font-size: 11px; line-height: 15px; letter-spacing: 2px;
    text-align: right;
  }
  .spine-title {
    position: absolute; left: 360px; top: 213px; width: 74px; height: 136px;
    writing-mode: vertical-rl; transform: rotate(180deg);
    text-align: center;
  }
  .spine-title .script { font-size: 17px; line-height: 18px; }
  .spine-title .bold { font-size: 20px; line-height: 18px; }
  .spine-author {
    position: absolute; left: 388px; top: 402px; height: 155px;
    writing-mode: vertical-rl; transform: rotate(180deg);
    font-size: 20px; letter-spacing: 5px;
  }

  /* Vorderseite */
  .author {
    position: absolute; left: 440px; width: 354px; top: 16px;
    text-align: center; font-size: 23px; letter-spacing: 5px;
  }
  .title { position: absolute; left: 440px; width: 354px; top: 62px; text-align: center; }
  .script {
    display: block;
    font-family: "Pinyon Script", cursive;
    color: var(--silver);
    font-size: 40px; line-height: 58px;
  }
  .bold {
    display: block;
    font-family: "Oswald", sans-serif; font-weight: 700;
    text-transform: uppercase; letter-spacing: -1px;
  }
  .title .rust { color: var(--rust); font-size: 56px; line-height: 56px; }
  .title .silver { color: var(--silver); font-size: 50px; line-height: 50px; }
  .spine-title .rust { color: var(--rust); }
  .spine-title .silver { color: var(--silver); }
  .heart-fire {
    position: absolute; left: 500px; top: 238px;
    width: 240px; height: 250px;
    background: radial-gradient(ellipse at 52% 50%, rgba(250,200,110,.95) 0%, rgba(240,150,60,.8) 18%, rgba(150,55,20,.55) 38%, rgba(90,30,12,.3) 58%, rgba(5,4,4,0) 74%);
  }
  .subtitle {
    position: absolute; left: 440px; width: 354px; top: 500px;
    text-align: center; font-size: 25px; line-height: 28px; letter-spacing: 4.5px;
  }
</style>
</head>
<body>
  <section class="spread">
    <div class="back-smoke" role="img" aria-label="Rot-schwarzer Rauch als Hintergrund des Klappentextes"></div>
    <p class="blurb">Lorem ipsum<br>dolor sit amet,<br>consectetur adipiscing<br>elit, sed do eiusmod<br>tempor incididunt ut labore<br>et dolore magna aliqua. Quis<br>ipsum suspendisse ultrices<br>gravida. Risus commodo<br>viverra maecenas accumsan<br>lacus vel facilisis. Lorem<br>ipsum dolor sit amet,<br>consectetur adipiscing<br>elit, sed do<br>eiusmod.</p>

    <p class="spine-subtitle thin">Verse zum Atemholen<br>für Suchende</p>
    <h2 class="spine-title">
      <span class="script">Kein Morgen trägt</span>
      <span class="bold rust">so leise</span>
      <span class="bold silver">fort</span>
    </h2>
    <p class="spine-author thin">Tobias Werhahn</p>

    <p class="author thin">Tobias Werhahn</p>
    <h1 class="title">
      <span class="script">Kein Morgen trägt</span>
      <span class="bold rust">so leise</span>
      <span class="bold silver">fort</span>
    </h1>
    <div class="heart-fire" role="img" aria-label="Liegendes Herz in Flammen, umgeben von rotem Rauch"></div>
    <p class="subtitle thin">Verse zum Atemholen<br>für Suchende</p>
  </section>
</body>
</html>
```